Gold Harbor Concierge

I need a website developed for our travel concierge service. I'm looking to be able to collect information and have the information collected directed to a inbox. I would also like to me able to manage the updates to the website myself. I also would like a mobile version of the website to be included. Our services include assistance with Bachelor Parties, Bachelorette Parties and Medical Tourism. We provide custom packages that include Airport Transportation, Lodging, Bilingual guides and any other special needs identified by our clients.
Industry/Entity Type
Travel
Coding
Coded - Design and coding required
Number of Pages Required
4 page
Look and feel

```html
<!DOCTYPE html>
<html lang="en">
<head>
<meta charset="utf-8">
<title>Gold Harbor Concierge</title>
<link href="https://fonts.googleapis.com/css2?family=Libre+Baskerville:wght@700&family=Poppins:ital,wght@0,400;0,500;0,600;1,400&display=swap" rel="stylesheet">
<style>
:root{
  --stage:#242424;
  --black:#000;
  --panel:#0b0b0b;
  --blue:#1ba6e0;
  --navy:#1d5ea8;
  --gold:#eaa72b;
  --amber:#d49b2a;
  --white:#fff;
  --muted:#b9b9b9;
  --field:#2b2b2b;
  --rule:#1e1e1e;
}
*{margin:0;padding:0;box-sizing:border-box}
html,body{width:720px;height:1200px;overflow:hidden;background:var(--stage)}
body{position:relative;font-family:"Poppins",sans-serif;color:var(--white)}
.abs{position:absolute}
.serif{font-family:"Libre Baskerville",serif;font-weight:700}
.photo{position:absolute;overflow:hidden}
.pill{position:absolute;border-radius:20px;font-weight:600;text-transform:uppercase;text-align:center;color:var(--white)}
.center{text-align:center}

/* Desktop */
.desktop{position:absolute;left:78px;top:117px;width:447px;height:966px;background:var(--black);overflow:hidden}
.brand{position:absolute;font-family:"Libre Baskerville",serif;font-weight:700;color:var(--gold)}
.topbar{left:201px;top:13px;font-size:4.4px;font-weight:600;color:var(--gold)}
.topbar span{color:var(--white)}
.social{position:absolute;border:1px solid var(--gold);border-radius:50%}
.badge{position:absolute;background:#4c9b2a;border-radius:2px}
.nav{position:absolute;left:67px;top:28px;width:312px;height:11px;background:var(--navy);display:flex;align-items:center;font-size:3.2px;font-weight:600;color:var(--white)}
.nav .item{padding-left:9px}
.nav .sep{padding-left:9px;color:#cfe0f5}
.nav .book{margin-left:auto;height:11px;width:46px;background:var(--gold);display:flex;align-items:center;justify-content:center;clip-path:polygon(6% 0,100% 0,100% 100%,0 100%)}
.hero-title{left:67px;top:80px;font-size:12px;line-height:13px;width:200px}
.dot{position:absolute;width:4.5px;height:4.5px;border:0.7px solid var(--white);border-radius:50%}
.h2{position:absolute;left:0;width:100%;text-align:center;color:var(--blue);font-family:"Libre Baskerville",serif;font-weight:700}
.card-title{position:absolute;left:0;width:100%;text-align:center;font-family:"Libre Baskerville",serif;font-weight:700}
.icon{position:absolute;border-radius:50%}
.icon svg{width:100%;height:100%}
.vrule{position:absolute;width:0.6px;background:#262626}
.quote{font-style:italic;color:#d6d6d6}
.field{position:absolute;background:var(--field);color:#9a9a9a;padding-left:4px}
.footer-h{position:absolute;font-family:"Libre Baskerville",serif;font-weight:700}
.info{position:absolute;color:var(--white)}
.up{position:absolute;width:0;height:0;border-left:4px solid transparent;border-right:4px solid transparent;border-bottom:9px solid var(--gold)}

/* Mobile */
.mobile{position:absolute;left:544px;top:117px;width:98px;height:964px;background:var(--black);overflow:hidden}
</style>
</head>
<body>

<!-- ============ DESKTOP ============ -->
<main class="desktop">
  <!-- header -->
  <header>
    <div class="abs" style="left:67px;top:3px;width:14px;height:14px;border:1.2px solid var(--gold);border-radius:50%"></div>
    <div class="brand" style="left:67px;top:18px;font-size:4.6px">Gold Harbor Concierge</div>
    <div class="abs topbar">Custom Party Packages: <span>&#9742; 555-010-2040</span></div>
    <div class="social" style="left:307px;top:8px;width:11px;height:11px"></div>
    <div class="social" style="left:321px;top:8px;width:11px;height:11px"></div>
    <div class="badge" style="left:341px;top:9px;width:38px;height:10px"></div>
    <nav class="nav">
      <span class="item">HOME</span><span class="sep">//</span>
      <span class="item">ABOUT US</span><span class="sep">//</span>
      <span class="item">SERVICES</span><span class="sep">//</span>
      <span class="item">REVIEWS</span><span class="sep">//</span>
      <span class="item">NIGHTLIFE</span><span class="sep">//</span>
      <span class="item">GALLERY</span><span class="sep">//</span>
      <span class="item">CONTACT US</span>
      <span class="book">BOOK NOW</span>
    </nav>
  </header>

  <!-- hero -->
  <section>
    <div class="photo" role="img" aria-label="Friends celebrating at a pool party with inflatable floats" style="left:0;top:39px;width:447px;height:151px;background:linear-gradient(110deg,#2f5f78 0%,#3b6f86 30%,#7a5a3e 55%,#5b3b2c 75%,#2f3c46 100%)"></div>
    <div class="abs" style="left:0;top:39px;width:447px;height:151px;background:rgba(0,0,0,.18)"></div>
    <h1 class="abs serif hero-title">Gold Harbor Concierge plans the trip, the party and every detail.</h1>
    <div class="pill" style="left:67px;top:127px;width:37px;height:11px;line-height:11px;font-size:3.4px;background:var(--blue)">Contact us</div>
    <div class="dot" style="left:374px;top:93px"></div>
    <div class="dot" style="left:374px;top:100px;background:var(--white)"></div>
    <div class="dot" style="left:374px;top:107px"></div>
    <div class="dot" style="left:374px;top:114px"></div>
  </section>

  <!-- services -->
  <section>
    <h2 class="h2" style="top:208px;font-size:10px">Our services</h2>
    <div class="photo" role="img" aria-label="Group of friends at a bachelor party" style="left:67px;top:229px;width:100px;height:116px;background:linear-gradient(180deg,#4a3a40 0%,#7a2f3c 55%,#c8303d 100%)"></div>
    <div class="card-title" style="left:67px;width:100px;top:326px;font-size:7px">Bachelor parties</div>
    <div class="photo" role="img" aria-label="Women celebrating at a bachelorette party" style="left:173px;top:229px;width:100px;height:116px;background:linear-gradient(180deg,#9fb3cc 0%,#5f86b8 55%,#2e5f9f 100%)"></div>
    <div class="card-title" style="left:173px;width:100px;top:305px;font-size:7px">Bachelorette parties</div>
    <div class="pill" style="left:205px;top:323px;width:37px;height:10px;line-height:10px;font-size:3.2px;background:var(--gold)">Book now</div>
    <div class="photo" role="img" aria-label="Traveler relaxing in a car during a medical tourism trip" style="left:279px;top:229px;width:100px;height:116px;background:linear-gradient(180deg,#6b6f7e 0%,#8e4f5e 55%,#cf3b44 100%)"></div>
    <div class="card-title" style="left:279px;width:100px;top:326px;font-size:7px">Medical tourism</div>
  </section>

  <div class="abs" style="left:0;top:364px;width:447px;height:0.6px;background:var(--rule)"></div>

  <!-- additional services -->
  <section>
    <h2 class="h2" style="top:381px;font-size:10px">Additional services</h2>
    <div class="icon" style="left:102px;top:403px;width:30px;height:30px;background:var(--blue)">
      <svg viewBox="0 0 30 30"><path d="M8 16h14l-2 3H10z M12 11l5 5h-4l-3-5z M20 13h3v3h-3z" fill="#fff"/></svg>
    </div>
    <div class="card-title" style="left:67px;width:100px;top:438px;font-size:7px;line-height:10px">Airport<br>Transportation</div>
    <div class="vrule" style="left:170px;top:403px;height:51px"></div>
    <div class="icon" style="left:208px;top:403px;width:30px;height:30px;background:var(--navy)">
      <svg viewBox="0 0 30 30"><path d="M8 12l7-4 7 4z M9 13h12v9H9z" fill="#fff"/><path d="M11 15h2v2h-2z M14 15h2v2h-2z M17 15h2v2h-2z M11 18h2v2h-2z M14 18h2v2h-2z M17 18h2v2h-2z" fill="#1d5ea8"/></svg>
    </div>
    <div class="card-title" style="left:173px;width:100px;top:438px;font-size:7px">Lodging</div>
    <div class="vrule" style="left:276px;top:403px;height:51px"></div>
    <div class="icon" style="left:314px;top:403px;width:30px;height:30px;background:#5fb8c0">
      <svg viewBox="0 0 30 30"><path d="M9 8h9v14H9z" fill="#fff"/><path d="M11 11h5 M11 14h5 M11 17h3" stroke="#5fb8c0" stroke-width="1"/><circle cx="20" cy="19" r="3.5" fill="#fff"/></svg>
    </div>
    <div class="card-title" style="left:279px;width:100px;top:438px;font-size:7px;line-height:10px">Bilingual<br>Guides</div>

    <div class="h2" style="top:476px;font-size:12px;color:var(--amber)">Any other special needs?</div>
    <div class="h2" style="top:492px;font-size:10px">Call now: 555-010-2040</div>
  </section>

  <!-- gallery -->
  <section>
    <div class="photo" role="img" aria-label="Guests toasting at a nightclub" style="left:67px;top:518px;width:75px;height:65px;background:linear-gradient(135deg,#3a1c1a,#8a4a2c,#2a1412)"></div>
    <div class="photo" role="img" aria-label="Friends celebrating with balloons" style="left:67px;top:588px;width:75px;height:65px;background:linear-gradient(135deg,#2c3040,#5a4e58,#3a2a2a)"></div>
    <div class="photo" role="img" aria-label="Friends relaxing together at a house party" style="left:146px;top:518px;width:153px;height:135px;background:linear-gradient(135deg,#6a4a32,#3a2a24 50%,#1e1a1c)"></div>
    <div class="photo" role="img" aria-label="Crowd dancing under confetti" style="left:305px;top:518px;width:74px;height:65px;background:linear-gradient(135deg,#1a2230,#3c4454,#1a1e28)"></div>
    <div class="photo" role="img" aria-label="Women blowing glitter at a celebration" style="left:305px;top:588px;width:74px;height:65px;background:linear-gradient(135deg,#9aa2a4,#7a8488,#b8a6a6)"></div>
  </section>

  <!-- testimonials -->
  <section>
    <div class="photo" role="img" aria-label="Dimmed party crowd in the background" style="left:0;top:676px;width:447px;height:161px;background:linear-gradient(120deg,#1c1714,#2c231d 50%,#1a1512)"></div>
    <h2 class="h2" style="top:698px;font-size:10px">What our clients say</h2>
    <div class="photo" role="img" aria-label="Client portrait" style="left:210px;top:719px;width:27px;height:27px;border-radius:50%;border:1px solid var(--gold);background:radial-gradient(circle,#d8d2cc,#7a6a60)"></div>
    <div class="abs" style="left:75px;top:772px;width:7px;height:7px;border-left:0.8px solid #777;border-bottom:0.8px solid #777;transform:rotate(45deg)"></div>
    <div class="abs" style="left:366px;top:772px;width:7px;height:7px;border-right:0.8px solid #777;border-top:0.8px solid #777;transform:rotate(45deg)"></div>
    <p class="abs center quote" style="left:110px;top:751px;width:227px;font-size:3.7px;line-height:5.7px">Every weekend we plan was handled from the airport pickup to the last toast, and our guides made each city feel easy. The lodging was spotless, the schedule ran on time and the whole group wants to book again next year without changing a thing.</p>
    <div class="abs center" style="left:0;width:447px;top:775px;font-size:3.8px"><span style="color:var(--gold)">Dana Reyes</span> / Loyal Customer</div>
    <div class="pill" style="left:205px;top:790px;width:37px;height:11px;line-height:11px;font-size:3.2px;background:var(--blue)">View all</div>
  </section>

  <!-- footer -->
  <footer>
    <div class="footer-h" style="left:67px;top:859px;font-size:5.6px">Contact Us</div>
    <div class="info" style="left:67px;top:871px;font-size:4.8px"><span style="color:var(--gold)">&#9742;</span> (555) 010-2077</div>
    <div class="info" style="left:67px;top:881px;font-size:3.4px"><span style="color:var(--gold)">&#9993;</span> hello@goldharborconcierge.com</div>
    <div class="info" style="left:67px;top:891px;font-size:3.4px;line-height:5.4px;width:80px;padding-left:8px">Harbor Point Plaza,<br>210 Quayside Ave, Suite 14,<br>Bayview - 40210</div>
    <svg class="abs" style="left:67px;top:891px" width="4" height="5" viewBox="0 0 4 5"><path d="M2 5L0.4 2.4A1.8 1.8 0 1 1 3.6 2.4Z" fill="var(--gold)"/></svg>
    <div class="social" style="left:67px;top:919px;width:10px;height:10px"></div>
    <div class="social" style="left:81px;top:919px;width:10px;height:10px"></div>

    <div class="footer-h" style="left:160px;top:859px;font-size:5.6px">Send Us Message</div>
    <div class="field" style="left:160px;top:873px;width:70px;height:9px;font-size:3.3px;line-height:9px">Name</div>
    <div class="field" style="left:234px;top:873px;width:70px;height:9px;font-size:3.3px;line-height:9px">Email</div>
    <div class="field" style="left:309px;top:873px;width:70px;height:9px;font-size:3.3px;line-height:9px">Phone</div>
    <div class="field" style="left:160px;top:887px;width:219px;height:28px;font-size:3.3px;padding-top:3px">Message</div>
    <div class="pill" style="left:160px;top:920px;width:33px;height:11px;line-height:11px;font-size:3.2px;background:var(--gold)">Send</div>

    <div class="info" style="left:67px;top:944px;font-size:3.4px">© 2021 <span style="color:var(--gold)">Gold Harbor Concierge</span>. All Rights Reserved.</div>
    <div class="up" style="left:384px;top:938px"></div>
  </footer>
</main>

<!-- ============ MOBILE ============ -->
<main class="mobile">
  <header>
    <div class="abs" style="left:8px;top:3px;width:9px;height:9px;border:1px solid var(--gold);border-radius:50%"></div>
    <div class="brand" style="left:8px;top:14px;font-size:3.2px">Gold Harbor Concierge</div>
    <div class="abs" style="left:45px;top:10px;font-size:3.3px;font-weight:600"><span style="color:var(--gold)">&#9742;</span> 555-010-2040</div>
    <div class="abs" style="left:80px;top:7px;width:10px;height:10px;border-radius:50%;background:var(--gold)"></div>
    <div class="abs" style="left:82.5px;top:10px;width:5px;height:0.7px;background:#fff;box-shadow:0 1.5px 0 #fff,0 3px 0 #fff"></div>
  </header>

  <section>
    <div class="photo" role="img" aria-label="Friends celebrating at a pool party" style="left:0;top:24px;width:98px;height:61px;background:linear-gradient(110deg,#2f5f78,#6a5a48 55%,#2f3c46)"></div>
    <div class="abs serif center" style="left:6px;top:37px;width:86px;font-size:5px;line-height:7.2px">Gold Harbor Concierge plans every detail of your trip.</div>
    <div class="pill" style="left:33px;top:63px;width:32px;height:7px;line-height:7px;font-size:2.4px;background:var(--gold)">Contact us</div>
  </section>

  <section>
    <h2 class="h2" style="top:92px;font-size:6px">Our services</h2>
    <div class="photo" role="img" aria-label="Group of friends at a bachelor party" style="left:8px;top:105px;width:82px;height:95px;background:linear-gradient(180deg,#4a3a40,#7a2f3c 55%,#c8303d)"></div>
    <div class="card-title" style="left:8px;width:82px;top:189px;font-size:4.6px">Bachelor parties</div>
    <div class="photo" role="img" aria-label="Women celebrating at a bachelorette party" style="left:8px;top:204px;width:82px;height:95px;background:linear-gradient(180deg,#9fb3cc,#5f86b8 55%,#2e5f9f)"></div>
    <div class="card-title" style="left:8px;width:82px;top:270px;font-size:4.6px">Bachelorette parties</div>
    <div class="pill" style="left:33px;top:280px;width:32px;height:7px;line-height:7px;font-size:2.4px;background:var(--gold)">Book now</div>
    <div class="photo" role="img" aria-label="Traveler relaxing in a car" style="left:8px;top:304px;width:82px;height:95px;background:linear-gradient(180deg,#6b6f7e,#8e4f5e 55%,#cf3b44)"></div>
    <div class="card-title" style="left:8px;width:82px;top:388px;font-size:4.6px">Medical tourism</div>
  </section>

  <section>
    <h2 class="h2" style="top:406px;font-size:5.6px">Additional services</h2>
    <div class="icon" style="left:36px;top:419px;width:27px;height:27px;background:var(--blue)">
      <svg viewBox="0 0 30 30"><path d="M8 16h14l-2 3H10z M12 11l5 5h-4l-3-5z M20 13h3v3h-3z" fill="#fff"/></svg>
    </div>
    <div class="card-title" style="top:449px;font-size:3.6px">Airport Transportation</div>
    <div class="abs" style="left:8px;top:462px;width:82px;height:0.6px;background:#262626"></div>
    <div class="icon" style="left:36px;top:468px;width:27px;height:27px;background:var(--navy)">
      <svg viewBox="0 0 30 30"><path d="M8 12l7-4 7 4z M9 13h12v9H9z" fill="#fff"/><path d="M11 15h2v2h-2z M14 15h2v2h-2z M17 15h2v2h-2z M11 18h2v2h-2z M14 18h2v2h-2z M17 18h2v2h-2z" fill="#1d5ea8"/></svg>
    </div>
    <div class="card-title" style="top:498px;font-size:3.6px">Lodging</div>
    <div class="abs" style="left:8px;top:511px;width:82px;height:0.6px;background:#262626"></div>
    <div class="icon" style="left:36px;top:517px;width:27px;height:27px;background:#5fb8c0">
      <svg viewBox="0 0 30 30"><path d="M9 8h9v14H9z" fill="#fff"/><path d="M11 11h5 M11 14h5 M11 17h3" stroke="#5fb8c0" stroke-width="1"/><circle cx="20" cy="19" r="3.5" fill="#fff"/></svg>
    </div>
    <div class="card-title" style="top:547px;font-size:3.6px">Bilingual Guides</div>
    <div class="h2" style="top:562px;font-size:3.8px;color:var(--amber)">Any other special needs?</div>
    <div class="h2" style="top:569px;font-size:5.6px">Call now: 555-010-2040</div>
  </section>

  <section>
    <div class="photo" role="img" aria-label="Friends relaxing together at a house party" style="left:4px;top:582px;width:90px;height:79px;background:linear-gradient(135deg,#6a4a32,#3a2a24 50%,#1e1a1c)"></div>
    <div class="abs" style="left:41px;top:658px;width:7px;height:7px;border-radius:50%;background:var(--gold)"></div>
    <div class="abs" style="left:51px;top:658px;width:7px;height:7px;border-radius:50%;background:var(--gold)"></div>
  </section>

  <section>
    <div class="photo" role="img" aria-label="Dimmed party crowd in the background" style="left:0;top:671px;width:98px;height:122px;background:linear-gradient(120deg,#1c1714,#2c231d 50%,#1a1512)"></div>
    <h2 class="h2" style="top:678px;font-size:5.6px">What our clients say</h2>
    <div class="photo" role="img" aria-label="Client portrait" style="left:38px;top:693px;width:22px;height:22px;border-radius:50%;border:1px solid var(--gold);background:radial-gradient(circle,#d8d2cc,#7a6a60)"></div>
    <p class="abs center quote" style="left:7px;top:720px;width:84px;font-size:2.6px;line-height:4.9px">Every weekend we plan was handled from the airport pickup to the last toast, and our guides made each city feel easy. The lodging was spotless and the whole group wants to book again next year.</p>
    <div class="abs center" style="left:0;width:98px;top:763px;font-size:2.8px"><span style="color:var(--gold)">Dana Reyes</span> / Loyal Customer</div>
    <div class="pill" style="left:33px;top:776px;width:32px;height:7px;line-height:7px;font-size:2.4px;background:var(--gold)">View all</div>
  </section>

  <footer>
    <div class="footer-h" style="left:8px;top:803px;font-size:4.6px">Contact Us</div>
    <div class="info" style="left:8px;top:814px;font-size:3.8px"><span style="color:var(--gold)">&#9742;</span> (555) 010-2077</div>
    <div class="info" style="left:8px;top:822px;font-size:2.8px"><span style="color:var(--gold)">&#9993;</span> hello@goldharborconcierge.com</div>
    <div class="info" style="left:8px;top:831px;font-size:2.8px;line-height:4.6px;width:80px;padding-left:7px">Harbor Point Plaza,<br>210 Quayside Ave, Suite 14,<br>Bayview - 40210</div>
    <div class="social" style="left:8px;top:850px;width:9px;height:9px"></div>
    <div class="social" style="left:20px;top:850px;width:9px;height:9px"></div>
    <div class="footer-h" style="left:8px;top:869px;font-size:4.6px">Send Us Message</div>
    <div class="field" style="left:8px;top:880px;width:82px;height:7px;font-size:2.6px;line-height:7px">Name</div>
    <div class="field" style="left:8px;top:890px;width:82px;height:7px;font-size:2.6px;line-height:7px">Email</div>
    <div class="field" style="left:8px;top:900px;width:82px;height:7px;font-size:2.6px;line-height:7px">Phone</div>
    <div class="field" style="left:8px;top:910px;width:82px;height:18px;font-size:2.6px;padding-top:2px">Message</div>
    <div class="pill" style="left:8px;top:932px;width:29px;height:8px;line-height:8px;font-size:2.6px;background:var(--gold)">Send</div>
    <div class="info" style="left:8px;top:951px;font-size:2.5px">© 2021 <span style="color:var(--gold)">Gold Harbor Concierge</span>. All Rights Reserved.</div>
    <div class="up" style="left:85px;top:948px;border-left-width:2.5px;border-right-width:2.5px;border-bottom-width:6px"></div>
  </footer>
</main>

</body>
</html>
```